Design a card that will be used for an e-gift card sold to customers.

I need to design the front an e-gift card for my pizza store. I picked the business card because it fits the same size as an e-gift card. I need the design and then I will submit to e-gift card company to produce. Looking for a fresh look that will appear cool, trendy to customer. Prefer to keep it to black and white but can add a bright green color.

Target Market(s)

My pizza store customers

Industry/Entity Type

Business

Contact Information for Business Card

I want the name Brightwell Pizza

Font styles to use
Sans Serif

Colors
9bcb3c

Requirements
Must have
• Brightwell Pizza
• Linden Hollow
Nice to have
• I would like a black background. Maybe Brightwell Pizza in white and the location, Linden Hollow. Maybe faded in background are words like, pizza, salads, wings, pepperoni, etc...or cartoon type pictures like pizza slices, fun pics. Would like to keep black and white shades but other colors are lighter greens.

```html
<!DOCTYPE html>
<html lang="en">
<head>
<meta charset="utf-8">
<title>Brightwell Pizza – Gift Card</title>
<link rel="stylesheet" href="https://fonts.googleapis.com/css2?family=Playfair+Display:wght@700;800&family=Lato:wght@300;400&family=Dancing+Script:wght@500&display=swap">
<style>
  :root {
    --backdrop: #2b2b2b;
    --card-black: #050505;
    --ink-grey: #6f6769;
    --rule-grey: #5a5557;
    --soft-grey: #7b7476;
  }
  html, body {
    margin: 0;
    width: 1200px;
    height: 1200px;
    overflow: hidden;
    background: var(--backdrop);
  }
  .gift-card {
    position: absolute;
    left: 100px;
    top: 315px;
    width: 1000px;
    height: 570px;
    border-radius: 42px;
    background: var(--card-black);
    overflow: hidden;
  }
  .tagline {
    position: absolute;
    left: 300px;
    top: 212px;
    margin: 0;
    font-family: "Lato", sans-serif;
    font-weight: 300;
    font-size: 20px;
    letter-spacing: 4px;
    color: var(--soft-grey);
  }
  .gift-line {
    position: absolute;
    left: 500px;
    top: 160px;
    margin: 0;
    font-family: "Dancing Script", cursive;
    font-weight: 500;
    font-size: 62px;
    line-height: 1.2;
    color: var(--soft-grey);
  }
  .divider {
    position: absolute;
    left: 0;
    top: 255px;
    width: 100%;
    height: 2px;
    background: var(--rule-grey);
  }
  .product-word {
    position: absolute;
    left: 460px;
    top: 222px;
    margin: 0;
    font-family: "Playfair Display", serif;
    font-weight: 800;
    font-size: 220px;
    line-height: 1;
    letter-spacing: -3px;
    color: var(--ink-grey);
    white-space: nowrap;
  }
  .brand-name {
    position: absolute;
    left: 48px;
    top: 290px;
    margin: 0;
    font-family: "Playfair Display", serif;
    font-weight: 700;
    font-size: 80px;
    line-height: 0.95;
    color: var(--ink-grey);
  }
  .location {
    position: absolute;
    left: 52px;
    top: 470px;
    margin: 0;
    font-family: "Lato", sans-serif;
    font-weight: 400;
    font-size: 17px;
    letter-spacing: 4px;
    color: var(--soft-grey);
  }
</style>
</head>
<body>
  <main class="gift-card">
    <p class="tagline">FRESH &amp; HOT</p>
    <p class="gift-line">Gift for you</p>
    <div class="divider"></div>
    <p class="product-word">PIZZA</p>
    <h1 class="brand-name">BRIGHT<br>WELL</h1>
    <p class="location">LINDEN HOLLOW</p>
  </main>
</body>
</html>
```